Velmora Athletics Trust website

Velmora athletics trust is a charity organisation that assists young athletes and clubs with the financial assistance they need to progress in their sporting career.

The organisation also establishes mentoring programs to community clubs and individuals.
We envision a home page with a horizontal navigation
Contact Us
Donate: A link to a secure payment system
Meet the team: A list of names and images of the board
Lastly the link to donate should be featured prominently and several times along with cues that lead people to find out more
We prefer limited scrolling and would like to see a clean yet modern design

I am unsure if it needs to be coded or not

Target Market(s)

Potential donors, applications for funds, potential affiliates

Industry/Entity Type

Charity

Coding

Coded - Design and coding required

Number of Pages Required

5+ page

Font styles to use
Sans Serif

Colors
3176b5
ec1f27
34a7d7

Requirements
Must have
• emotionally engaging and informative
• motion enabled pictures
• links to donate
• Music
• Enable video uploads
• Large horizontal pictures of young sports players prominently soccer at this stage
• Social media presence
Nice to have
• Live chat
Should not have
• Images that depict poverty

```html
<!DOCTYPE html>
<html lang="en">
<head>
<meta charset="utf-8">
<title>Velmora Athletics Trust</title>
<link href="https://fonts.googleapis.com/css2?family=Open+Sans:wght@400;600;700&family=Roboto+Condensed:wght@400;700&display=swap" rel="stylesheet">
<style>
:root{
  --red:#e8323a;
  --red-dark:#c9252c;
  --blue:#3176b5;
  --navy:#1f4f8f;
  --sky:#38a6d9;
  --sky-dark:#2b8fc0;
  --ink:#333;
  --muted:#888;
  --line:#dddddd;
  --paper:#f6f6f6;
  --card:#ececec;
  --backdrop:#263a55;
}
*{box-sizing:border-box;margin:0;padding:0}
html,body{width:1200px;height:3237px;overflow:hidden}
body{background:var(--backdrop);font-family:"Open Sans",sans-serif;color:var(--ink)}
.page{position:absolute;left:82px;top:22px;width:1036px;height:3215px;background:var(--paper)}
.abs{position:absolute}
a{color:inherit;text-decoration:none}

/* header */
.brand{left:14px;top:22px;display:flex;align-items:center;gap:14px}
.brand-dot{width:62px;height:62px;border-radius:50%;background:var(--blue)}
.brand-name{font-weight:700;font-size:26px;color:var(--red);letter-spacing:.5px}
.contact-top{left:576px;top:30px;display:flex;gap:14px;align-items:center;font-size:13px;color:#666;line-height:22px}
.btn-donate{display:inline-flex;align-items:center;gap:8px;background:var(--red);color:#fff;border-radius:22px;font-family:"Roboto Condensed",sans-serif;font-size:16px;padding:0 16px 0 10px;height:44px;box-shadow:0 2px 0 var(--red-dark)}
.btn-donate .coin{width:22px;height:22px;border:2px solid #fff;border-radius:50%;display:flex;align-items:center;justify-content:center;font-size:13px;font-weight:700}
.top-donate{left:885px;top:30px;width:130px;height:44px}

.main-nav{left:318px;top:108px;width:700px;height:65px;display:flex;background:var(--sky)}
.main-nav a{flex:1;display:flex;flex-direction:column;align-items:center;justify-content:center;gap:6px;color:#fff;font-size:12px;font-weight:600;letter-spacing:.3px;border-left:1px solid rgba(255,255,255,.2)}
.main-nav a.home{flex:0 0 114px;background:#ef6d72;border-left:0;clip-path:polygon(8% 0,100% 0,100% 100%,0 100%)}

/* hero */
.hero{left:15px;top:176px;width:1003px;height:460px;background:linear-gradient(180deg,#6d6a63 0%,#8b867a 40%,#4f8b3b 75%,#3f7d30 100%)}
.hero-panel{left:604px;top:104px;width:324px;height:248px;background:rgba(232,50,58,.92);border:3px solid rgba(255,255,255,.85);padding:16px 26px}
.hero-panel h1{font-family:"Roboto Condensed",sans-serif;font-weight:700;color:#fff;font-size:52px;line-height:56px}
.btn-reg{display:inline-block;margin-top:18px;border:2px solid #fff;color:#fff;font-size:13px;padding:8px 14px;letter-spacing:.5px}
.dots{display:flex;gap:8px;margin-top:12px}
.dots span{width:10px;height:10px;border-radius:50%;background:#fff}
.dots span:first-child{background:transparent;border:2px solid #fff}

/* audience cards */
.aud{top:653px;width:324px;height:281px;background:var(--card);border:1px solid #e0e0e0;text-align:center;padding-top:20px}
.aud .ico{width:104px;height:104px;border-radius:50%;background:var(--sky);margin:0 auto;display:flex;align-items:center;justify-content:center}
.aud h3{font-weight:400;font-size:17px;color:#555;margin-top:16px}
.aud p{font-size:11px;line-height:18px;color:#999;margin:6px 28px 0}
.more{display:inline-block;margin-top:14px;font-size:11px;color:#444;font-weight:600}

/* welcome */
.welcome{left:0;top:1014px;width:1036px;text-align:center}
.sec-title{font-weight:400;font-size:28px;letter-spacing:1px;color:#333}
.welcome p{font-size:11px;line-height:22px;color:#888;width:930px;margin:18px auto 0}
.welcome .btn-donate{margin-top:26px;height:47px}
.divider{left:0;top:1219px;width:1036px;height:1px;background:#e6e6e6}

/* projects */
.featured-title{left:0;top:1288px;width:1036px;text-align:center;font-size:26px}
.proj{top:1350px;width:234px;height:296px;background:#fff;border:1px solid var(--line);padding:4px;text-align:center}
.proj .ph{height:168px}
.proj h4{font-weight:400;font-size:15px;color:#555;margin-top:14px}
.proj p{font-size:11px;line-height:18px;color:#999;margin:6px 16px 0}

/* discover / testimonials */
.h-left{font-size:23px;font-weight:400;letter-spacing:.5px}
.video{left:15px;top:1773px;width:495px;height:298px;background:linear-gradient(180deg,#7a8a6e 0%,#6f8e57 55%,#557a3d 100%)}
.video-bar{left:0;top:0;width:100%;height:40px;background:rgba(40,40,40,.85);color:#fff;font-size:11px;padding:0 16px;display:flex;align-items:center;justify-content:space-between}
.play{left:222px;top:160px;width:52px;height:38px;border:2px solid #fff;border-radius:6px;background:rgba(0,0,0,.3);display:flex;align-items:center;justify-content:center}
.testi{left:544px;width:474px;display:flex;gap:26px}
.avatar{flex:0 0 104px;height:104px;border-radius:50%;background:linear-gradient(160deg,#b89a7c,#7b624d)}
.testi blockquote{font-style:italic;font-size:11px;line-height:20px;color:#777;margin-top:10px}
.testi blockquote::before{content:"\201C";font-size:26px;color:#555;line-height:0;vertical-align:-8px;margin-right:4px}
.testi .who{font-size:12px;color:var(--blue);margin-top:10px}
.stars{color:#e8a33a;font-size:11px;letter-spacing:1px}

/* news */
.news{left:15px;top:2147px;width:1003px;height:391px;background:linear-gradient(120deg,#1d4f93 0%,#2a66ad 50%,#1c4c8c 100%)}
.news h2{position:absolute;top:64px;width:100%;text-align:center;font-family:"Roboto Condensed",sans-serif;font-weight:700;font-size:30px;color:#fff}
.news-card{top:125px;width:442px;height:183px;background:#fff;display:flex;gap:16px;padding:12px}
.news-card .ph{flex:0 0 158px;height:159px}
.news-card h5{font-weight:400;font-size:13px;color:#333}
.news-card .date{font-style:italic;font-weight:700;font-size:12px;color:var(--navy);margin-top:12px}
.news-card p{font-size:11px;line-height:17px;color:#777;margin-top:8px}
.news-card .more{color:var(--navy);margin-top:8px}

/* partners */
.partners-title{left:0;top:2612px;width:1036px;text-align:center;font-size:27px}
.rule{left:478px;top:2661px;width:80px;height:2px;background:#ccc}
.badge{top:2708px;width:110px;height:36px;background:#c8c8c8;border-radius:3px}

/* footer */
.footer{left:15px;top:2812px;width:1003px;height:381px;background:#ececec}
.footer h6{font-weight:400;font-size:15px;letter-spacing:.5px;color:#333}
.field{width:245px;height:40px;background:#fff;border:1px solid #ddd;font-size:10px;color:#555;padding:12px;margin-top:12px}
.btn-submit{display:inline-block;margin-top:14px;background:var(--navy);color:#fff;font-size:11px;font-weight:700;padding:9px 18px}
.contact-list li{list-style:none;display:flex;gap:14px;font-size:11px;line-height:17px;color:#666;margin-top:16px}
.links li{list-style:none;font-size:10px;color:#777;line-height:22px}
.foot-brand{text-align:center}
.foot-brand .brand-dot{width:62px;height:62px;margin:0 auto}
.foot-brand .brand-name{font-size:16px;margin-top:8px}
.btn-chat{display:inline-block;margin-top:16px;background:var(--navy);color:#fff;font-size:12px;font-weight:700;padding:8px 22px}
.foot-rule{left:24px;top:235px;width:955px;height:1px;background:#dcdcdc}
.socials{left:0;top:256px;width:100%;display:flex;justify-content:center;gap:4px}
.socials span{width:24px;height:24px;border-radius:50%;border:2px solid var(--blue);background:#fff}
.socials span:last-child{border-color:var(--red)}
.copy{left:0;top:334px;width:100%;text-align:center;font-size:10px;color:#666}
</style>
</head>
<body>
<div class="page">

  <header>
    <a class="brand abs" href="#"><span class="brand-dot"></span><span class="brand-name">Velmora Trust</span></a>
    <div class="contact-top abs">
      <svg width="26" height="26" viewBox="0 0 24 24"><path fill="#666" d="M6.6 10.8a15 15 0 0 0 6.6 6.6l2.2-2.2c.3-.3.7-.4 1-.2 1.1.4 2.3.6 3.6.6.6 0 1 .4 1 1V20c0 .6-.4 1-1 1A17 17 0 0 1 3 4c0-.6.4-1 1-1h3.5c.6 0 1 .4 1 1 0 1.3.2 2.5.6 3.6.1.3 0 .7-.2 1z"/></svg>
      <div>info@velmoratrust.org<br>Phone : (555) - 014 - 2290</div>
    </div>
    <a class="btn-donate top-donate abs" href="#"><span class="coin">$</span>DONATE NOW</a>
    <nav class="main-nav abs">
      <a class="home" href="#"><svg width="18" height="16" viewBox="0 0 18 16"><path fill="#fff" d="M9 0 0 8h3v8h4v-5h4v5h4V8h3z"/></svg>HOME</a>
      <a href="#"><svg width="16" height="16" viewBox="0 0 16 16"><rect x="1" y="2" width="14" height="13" rx="1" fill="none" stroke="#fff" stroke-width="1.6"/><path d="M1 6h14" stroke="#fff" stroke-width="1.6"/></svg>PROGRAM</a>
      <a href="#"><svg width="18" height="16" viewBox="0 0 18 16"><path d="M1 1h7l9 9-6 5-9-9z" fill="none" stroke="#fff" stroke-width="1.6"/><circle cx="5" cy="5" r="1.4" fill="#fff"/></svg>DONATE</a>
      <a href="#"><svg width="18" height="16" viewBox="0 0 18 16"><path d="M6 1 1 4l2 4 2-1v8h8V7l2 1 2-4-5-3c0 2-1 3-3 3S6 3 6 1z" fill="none" stroke="#fff" stroke-width="1.5"/></svg>MEET THE TEAM</a>
      <a href="#"><svg width="18" height="14" viewBox="0 0 18 14"><rect x="1" y="1" width="16" height="12" fill="none" stroke="#fff" stroke-width="1.6"/><path d="m1 1 8 7 8-7" fill="none" stroke="#fff" stroke-width="1.6"/></svg>CONTACT US</a>
    </nav>
  </header>

  <section class="hero abs" role="img" aria-label="Young soccer player in a red kit celebrating with a ball in a packed stadium">
    <div class="hero-panel abs">
      <h1>Velmora Athletics Trust</h1>
      <a class="btn-reg" href="#">REGISTRATION ▾</a>
      <div class="dots"><span></span><span></span><span></span><span></span></div>
    </div>
  </section>

  <section>
    <article class="aud abs" style="left:15px">
      <div class="ico"><svg width="54" height="40" viewBox="0 0 54 40"><circle cx="27" cy="11" r="7" fill="#fff"/><circle cx="10" cy="14" r="5" fill="#fff"/><circle cx="44" cy="14" r="5" fill="#fff"/><path d="M15 38c0-9 5-16 12-16s12 7 12 16z" fill="#fff"/><path d="M1 36c0-7 4-12 9-12 3 0 5 1 6 3-2 3-3 6-3 9zM53 36c0-7-4-12-9-12-3 0-5 1-6 3 2 3 3 6 3 9z" fill="#fff"/></svg></div>
      <h3>Community Clubs</h3>
      <p>Sed ut perspiciatis unde omnis iste natus error sit voluptatem accusantium doloremque laudantium, totam rem aperiam, eaque ipsa quae</p>
      <a class="more" href="#">READ MORE ➜</a>
    </article>
    <article class="aud abs" style="left:356px">
      <div class="ico"><svg width="40" height="44" viewBox="0 0 40 44"><circle cx="20" cy="12" r="10" fill="#fff"/><path d="M2 44c0-12 8-20 18-20s18 8 18 20z" fill="#fff"/></svg></div>
      <h3>Individuals</h3>
      <p>Sed ut perspiciatis unde omnis iste natus error sit voluptatem accusantium doloremque laudantium, totam rem aperiam, eaque ipsa quae</p>
      <a class="more" href="#">READ MORE ➜</a>
    </article>
    <article class="aud abs" style="left:697px">
      <div class="ico"><svg width="34" height="46" viewBox="0 0 34 46"><rect x="8" y="0" width="18" height="6" fill="#fff"/><rect x="2" y="8" width="30" height="38" rx="4" fill="#fff"/><text x="17" y="34" text-anchor="middle" font-family="Open Sans,sans-serif" font-weight="700" font-size="18" fill="#38a6d9">$</text></svg></div>
      <h3>Donate</h3>
      <p>Sed ut perspiciatis unde omnis iste natus error sit voluptatem accusantium doloremque laudantium, totam rem aperiam, eaque ipsa quae</p>
      <a class="more" href="#">READ MORE ➜</a>
    </article>
  </section>

  <section class="welcome abs">
    <h2 class="sec-title" style="font-size:30px">WELCOME TO VELMORA TRUST</h2>
    <p>Sed ut perspiciatis unde omnis iste natus error sit voluptatem accusantium doloremque laudantium, totam rem aperiam, eaque ipsa quae ab illo inventore veritatis et quasi architecto beatae vitae dicta sunt explicabo. Nemo enim ipsam voluptatem quia voluptas sit aspernatur aut odit aut fugit, sed quia consequuntur magni dolores eos qui ratione voluptatem sequi nesciunt. Neque porro quisquam est, qui dolorem ipsum quia dolor sit amet, consectetur, adipisci velit, sed quia non numquam</p>
    <a class="btn-donate" href="#"><span class="coin">$</span>DONATE NOW</a>
  </section>
  <div class="divider abs"></div>

  <h2 class="sec-title featured-title abs">FEATURED PROJECTS</h2>
  <article class="proj abs" style="left:15px"><div class="ph" role="img" aria-label="Child learning with a teacher at an easel" style="background:linear-gradient(135deg,#c9a887,#8a6a52)"></div><h4>Sed ut perspiciatis unde</h4><p>Mauris vel lacus vitae felis vestibulum volutpat imperdiet ac nisl Cum sociis natoque sodales velit</p></article>
  <article class="proj abs" style="left:271px"><div class="ph" role="img" aria-label="Young goalkeeper in yellow on a soccer pitch" style="background:linear-gradient(180deg,#8a9a7a,#5e8a42)"></div><h4>Sed ut perspiciatis unde</h4><p>Mauris vel lacus vitae felis vestibulum volutpat imperdiet ac nisl Cum sociis natoque sodales velit</p></article>
  <article class="proj abs" style="left:527px"><div class="ph" role="img" aria-label="Children playing in a school band" style="background:linear-gradient(135deg,#c98a6a,#8f4f3a)"></div><h4>Sed ut perspiciatis unde</h4><p>Mauris vel lacus vitae felis vestibulum volutpat imperdiet ac nisl Cum sociis natoque sodales velit</p></article>
  <article class="proj abs" style="left:783px"><div class="ph" role="img" aria-label="Kids in red kits chasing a soccer ball" style="background:linear-gradient(180deg,#b35a5a,#5f8f45)"></div><h4>Sed ut perspiciatis unde</h4><p>Mauris vel lacus vitae felis vestibulum volutpat imperdiet ac nisl Cum sociis natoque sodales velit</p></article>

  <h2 class="h-left abs" style="left:15px;top:1728px">DISCOVER A PROJECT</h2>
  <div class="video abs" role="img" aria-label="Video of youth soccer players competing for the ball">
    <div class="video-bar abs"><span>Velmora Trust</span><svg width="14" height="14" viewBox="0 0 14 14"><circle cx="11" cy="3" r="2" fill="#fff"/><circle cx="3" cy="7" r="2" fill="#fff"/><circle cx="11" cy="11" r="2" fill="#fff"/><path d="M11 3 3 7l8 4" stroke="#fff" fill="none"/></svg></div>
    <div class="play abs"><svg width="16" height="18" viewBox="0 0 16 18"><path d="M0 0l16 9-16 9z" fill="#fff"/></svg></div>
  </div>

  <h2 class="h-left abs" style="left:544px;top:1728px">TESTIMONIALS</h2>
  <svg class="abs" style="left:988px;top:1734px" width="30" height="18" viewBox="0 0 30 18"><path d="M10 2 3 9l7 7M20 2l7 7-7 7" stroke="#444" stroke-width="3" fill="none"/></svg>
  <div class="testi abs" style="top:1796px">
    <div class="avatar" role="img" aria-label="Portrait of a supporter"></div>
    <div><blockquote>Nemo enim ipsam voluptatem quia voluptas sit aspernatur aut odit aut fugit, sed quia consequuntur magni dolores eos qui ratione voluptatem sequi nesciunt.</blockquote><div class="who">John doe - Velmora Trust</div><div class="stars">★★★☆☆</div></div>
  </div>
  <div class="testi abs" style="top:1963px">
    <div class="avatar" role="img" aria-label="Portrait of a supporter" style="background:linear-gradient(160deg,#c9a98a,#8a6c55)"></div>
    <div><blockquote>Nemo enim ipsam voluptatem quia voluptas sit aspernatur aut odit aut fugit, sed quia consequuntur magni dolores eos qui ratione voluptatem sequi nesciunt.</blockquote><div class="who">John doe - Velmora Trust</div><div class="stars">★★★☆☆</div></div>
  </div>

  <section class="news abs">
    <h2>LATEST NEWS AND EVENTS</h2>
    <article class="news-card abs" style="left:48px">
      <div class="ph" role="img" aria-label="Youth team sitting together on the grass" style="background:linear-gradient(180deg,#7c8a7a,#4f6f3f)"></div>
      <div><h5>Nulla at diam ornare, aliquam urna</h5><div class="date">MAY 25, 2016</div><p>Nulla at diam ornare, aliquam urna vel, modo urna. Nam id risus a est luctus consectetur quis eget libero. Suspendisse potenti.</p><a class="more" href="#">READ MORE ➜</a></div>
    </article>
    <article class="news-card abs" style="left:518px">
      <div class="ph" role="img" aria-label="Close-up of a player's boot striking a soccer ball" style="background:linear-gradient(180deg,#5a6a7a,#4a7a3a)"></div>
      <div><h5>Nulla at diam ornare, aliquam urna</h5><div class="date">MAY 25, 2016</div><p>Nulla at diam ornare, aliquam urna vel, modo urna. Nam id risus a est luctus consectetur quis eget libero. Suspendisse potenti.</p><a class="more" href="#">READ MORE ➜</a></div>
    </article>
  </section>

  <h2 class="sec-title partners-title abs">OUR PARTNERS AND SUPPORTERS</h2>
  <div class="rule abs"></div>
  <div class="badge abs" style="left:35px"></div>
  <div class="badge abs" style="left:201px"></div>
  <div class="badge abs" style="left:367px"></div>
  <div class="badge abs" style="left:533px"></div>
  <div class="badge abs" style="left:699px"></div>
  <div class="badge abs" style="left:865px"></div>

  <footer class="footer abs">
    <div class="abs" style="left:24px;top:60px">
      <h6>KEEP IN TOUCH</h6>
      <div class="field">Enter name</div>
      <div class="field">Enter email</div>
      <a class="btn-submit" href="#">SUBMIT</a>
    </div>
    <div class="abs" style="left:352px;top:60px">
      <h6>CONTACT US</h6>
      <ul class="contact-list">
        <li><svg width="12" height="16" viewBox="0 0 12 16"><path d="M6 0a6 6 0 0 0-6 6c0 4 6 10 6 10s6-6 6-10a6 6 0 0 0-6-6z" fill="#666"/><circle cx="6" cy="6" r="2" fill="#ececec"/></svg><span>Velmora athletics trust<br>48 Linden Row, Ashford, Nc.<br>27000</span></li>
        <li><svg width="12" height="14" viewBox="0 0 24 24"><path fill="#666" d="M6.6 10.8a15 15 0 0 0 6.6 6.6l2.2-2.2c.3-.3.7-.4 1-.2 1.1.4 2.3.6 3.6.6.6 0 1 .4 1 1V20c0 .6-.4 1-1 1A17 17 0 0 1 3 4c0-.6.4-1 1-1h3.5c.6 0 1 .4 1 1 0 1.3.2 2.5.6 3.6.1.3 0 .7-.2 1z"/></svg><span>Phone:&nbsp; 555-016-4473</span></li>
        <li><svg width="12" height="10" viewBox="0 0 12 10"><rect width="12" height="10" fill="#666"/><path d="m0 0 6 5 6-5" stroke="#ececec" fill="none"/></svg><span>Email: hello@velmoratrust.org</span></li>
      </ul>
    </div>
    <div class="abs" style="left:663px;top:60px">
      <h6>QUICK LINKS</h6>
      <ul class="links" style="margin-top:10px"><li>Home</li><li>About Us</li><li>Program</li><li>Donate</li><li>Meet the Team</li><li>Contact Us</li></ul>
    </div>
    <div class="foot-brand abs" style="left:779px;top:60px;width:170px">
      <span class="brand-dot" style="display:block"></span>
      <div class="brand-name">Velmora Trust</div>
      <a class="btn-chat" href="#">LIVE CHAT</a>
    </div>
    <div class="foot-rule abs"></div>
    <div class="socials abs"><span></span><span></span><span></span><span></span></div>
    <div class="copy abs">©2015 - 2016 Velmora Trust, All Rights Reserved.</div>
  </footer>

</div>
</body>
</html>
```